Whiskey Glass Packaging Design Project

I require a package design for my products - Whiskey Tasting glasses ( Set of 4) I will be selling on the Brevora USA platform. Must be of high quality, something that the customer will be very impressed with after opening once it arrives at their doorstop. To get an idea of competition please take a look on Brevora.com and do a search on Whiskey Glasses - Scotch Glasses. The competition is very good so we require something that will be better than them. We have a home and kitchen brand that caters to an audience that appreciate fine whiskey / oak barrels / cigars ... I can provide logo and content to be placed on box as well as dine line.

Target Market(s)

Men who love all things about Whiskey / Business / Cigars. Men / Women / Wives / Husbands who are looking to buy gifts for Husband / Partner .

Requirements
Must have
• On one side of the box we would like for the following wording to be included.
The KERAVIND snifter glass is one of the ideal glasses that all enthusiasts will swear by. The glass is a type of stemware, a short - stemmed glass whose vessel has a wide bottom and a relatively narrow top. It is mostly used to serve aged brown Scotch / Whiskey, Bourbon and Brandy.
It's simply a matter of raising the glass to take in a whiff of the aromas before taking a sip. We hope the graceful design of this KERAVIND Whiskey glass adds a nice touch of class to the presentation of your favourite drop ! Enjoy !
Nice to have
• Elegant, soothing and relaxing feel.
Should not have
• Nothing aggressive, racist, homosexual / anti gay .

```html
<!DOCTYPE html>
<html lang="en">
<head>
<meta charset="utf-8">
<title>KERAVIND Whiskey Glasses – Box Dieline</title>
<link rel="stylesheet" href="https://fonts.googleapis.com/css2?family=Roboto+Condensed:wght@300;400&family=Cormorant+Garamond:ital,wght@1,500&display=swap">
<style>
  :root {
    --paper: #ffffff;
    --panel: #dcdde0;
    --flap-top: #e6e7e9;
    --flap-bottom: #d3d4d7;
    --cut-line: #3a3a3c;
    --ink: #1f1f21;
    --gold: #b89a5c;
    --gold-deep: #a8884b;
    --gold-glow: #f4edc8;
    --logo-box: #262527;
  }
  html, body {
    margin: 0;
    padding: 0;
    width: 1200px;
    height: 572px;
    overflow: hidden;
    background: var(--paper);
  }
  .dieline {
    display: block;
    width: 1200px;
    height: 572px;
  }
  .cut { fill: none; stroke: var(--cut-line); stroke-width: 1.6; }
  .panel-face { fill: var(--panel); }
  .flap-face { fill: url(#flapShade); stroke: var(--cut-line); stroke-width: 1.6; }
  .tab-face { fill: var(--panel); stroke: var(--cut-line); stroke-width: 1.6; }
  .logo-box { fill: var(--logo-box); }
  .brand-name {
    font-family: "Roboto Condensed", sans-serif;
    font-weight: 400;
    fill: var(--gold);
    text-anchor: middle;
  }
  .product-title {
    font-family: "Roboto Condensed", sans-serif;
    font-weight: 400;
    fill: var(--ink);
    text-anchor: middle;
  }
  .product-title .accent { fill: var(--gold); }
  .qty-label, .qty-number {
    font-family: "Roboto Condensed", sans-serif;
    font-weight: 400;
    fill: var(--ink);
    text-anchor: middle;
  }
  .story {
    font-family: "Cormorant Garamond", serif;
    font-style: italic;
    font-weight: 500;
    font-size: 17px;
    fill: #2c2c2e;
  }
</style>
</head>
<body>
<svg class="dieline" viewBox="0 0 2560 1220" xmlns="http://www.w3.org/2000/svg" aria-label="KERAVIND whiskey glasses box, flat dieline">
  <defs>
    <linearGradient id="flapShade" x1="0" y1="0" x2="0" y2="1">
      <stop offset="0" stop-color="var(--flap-top)"/>
      <stop offset="1" stop-color="var(--flap-bottom)"/>
    </linearGradient>
    <radialGradient id="photoGlow" cx="0.45" cy="0.4" r="0.7">
      <stop offset="0" stop-color="var(--gold-glow)"/>
      <stop offset="0.35" stop-color="#d4bd85"/>
      <stop offset="1" stop-color="var(--gold-deep)"/>
    </radialGradient>

    <!-- dust flap with tuck tab (wide panels) -->
    <g id="tuckFlap">
      <path class="tab-face" d="M138,107 L138,52 L173,17 L387,17 L401,31 L401,55 A7,7 0 0 0 415,55 L415,31 L429,17 L643,17 L680,52 L680,107 Z"/>
      <rect class="flap-face" x="101" y="103" width="615" height="312"/>
    </g>

    <!-- rounded dust flap with slot (narrow panels) -->
    <g id="slotFlap">
      <path class="flap-face" d="M726,415 L726,50 Q726,22 754,22 L1290,22 Q1318,22 1318,50 L1318,415 Z"/>
      <line class="cut" x1="726" y1="113" x2="1318" y2="113"/>
      <rect class="cut" x="1015" y="68" width="14" height="315" rx="7"/>
    </g>

    <!-- front face -->
    <g id="frontFace">
      <rect class="panel-face" x="101" y="415" width="615" height="395"/>
      <rect x="285" y="415" width="431" height="395" fill="url(#photoGlow)" role="img" aria-label="Product photo: two whiskey snifter glasses glowing on a warm gold background"/>
      <rect class="logo-box" x="200" y="513" width="170" height="169"/>
      <text class="brand-name" x="285" y="632" font-size="17" letter-spacing="4">KERAVIND</text>
      <text class="product-title" x="285" y="710" font-size="30">Whiskey <tspan class="accent">Glasses</tspan></text>
    </g>
  </defs>

  <!-- glue flap -->
  <path class="tab-face" d="M101,415 L12,465 L12,757 L101,810 Z"/>

  <!-- top and bottom flaps -->
  <use href="#tuckFlap"/>
  <use href="#tuckFlap" transform="translate(0,1225) scale(1,-1)"/>
  <use href="#slotFlap"/>
  <use href="#slotFlap" transform="translate(0,1225) scale(1,-1)"/>
  <use href="#tuckFlap" transform="translate(1228,0)"/>
  <use href="#tuckFlap" transform="translate(1228,1225) scale(1,-1)"/>
  <use href="#slotFlap" transform="translate(1228,0)"/>
  <use href="#slotFlap" transform="translate(1228,1225) scale(1,-1)"/>

  <!-- main body band -->
  <rect class="panel-face" x="101" y="415" width="2455" height="395"/>

  <!-- front panels -->
  <use href="#frontFace"/>
  <use href="#frontFace" transform="translate(1228,0)"/>

  <!-- side panel: quantity -->
  <g class="side-qty">
    <rect class="logo-box" x="989" y="494" width="71" height="71"/>
    <text class="brand-name" x="1024.5" y="544" font-size="8" letter-spacing="1.5">KERAVIND</text>
    <text class="product-title" x="1026" y="600" font-size="28">Whiskey <tspan class="accent">Glasses</tspan></text>
    <text class="qty-label" x="1026" y="673" font-size="32">QTY</text>
    <line x1="1003" y1="685" x2="1050" y2="685" stroke="var(--ink)" stroke-width="2.5"/>
    <text class="qty-number" x="1026" y="752" font-size="80">4</text>
  </g>

  <!-- side panel: story -->
  <g class="side-story">
    <rect class="logo-box" x="2217" y="494" width="71" height="71"/>
    <text class="brand-name" x="2252.5" y="544" font-size="8" letter-spacing="1.5">KERAVIND</text>
    <text class="story" x="2000" y="592">The KERAVIND snifter glass is one of the ideal glasses that all enthusiasts will</text>
    <text class="story" x="2000" y="615">swear by. The glass is a type of stemware, a short - stemmed glass whose vessel</text>
    <text class="story" x="2000" y="638">has a wide bottom and a relatively narrow top. It is mostly used to serve aged</text>
    <text class="story" x="2000" y="661">brown Scotch / Whiskey, Bourbon and Brandy.</text>
    <text class="story" x="2000" y="684">It's simply a matter of raising the glass to take in a whiff of the aromas before</text>
    <text class="story" x="2000" y="707">taking a sip. We hope the graceful design of this KERAVIND Whiskey glass</text>
    <text class="story" x="2000" y="730">adds a nice touch of class to the presentation of your favourite drop ! Enjoy !</text>
  </g>

  <!-- body outline and folds -->
  <rect class="cut" x="101" y="415" width="2455" height="395"/>
  <line class="cut" x1="716" y1="415" x2="716" y2="810"/>
  <line class="cut" x1="1329" y1="415" x2="1329" y2="810"/>
  <line class="cut" x1="1944" y1="415" x2="1944" y2="810"/>
</svg>
</body>
</html>
```